Name of business RTV Harbor Management Group, LP.
business focuses on hotel investments and real estate deals, on the bottom of the card I need my partner company listed as "Strategic Partner of Velor Hotel Group" www.velorhotelgroup-example.com and the logo that is attached for them on the bottom also

I am the Principal of the business

Industry/Entity Type

Real Estate

Contact Information for Business Card

Darnell Quibey
287 Wexford Avenue
Lebanon, TN 37185
C- 615-302-4418
D- 615-719-2083
F- 615-864-3371

```html
<!DOCTYPE html>
<html lang="en">
<head>
<meta charset="utf-8">
<title>RTV Harbor Management Group — Business Card</title>
<link rel="stylesheet" href="https://fonts.googleapis.com/css2?family=Exo+2:wght@400;500;700&display=swap">
<style>
  :root {
    --slate: #3f5268;
    --band-light: #e9eaeb;
    --panel-grey: #d6d7d8;
    --ink-navy: #1c1f6b;
    --partner-blue: #1aa9e0;
    --white: #ffffff;
    --backdrop: #e4e6e9;
  }
  html, body {
    margin: 0;
    width: 1200px;
    height: 1000px;
    overflow: hidden;
    background: var(--backdrop);
  }
  .business-card {
    position: absolute;
    left: 75px;
    top: 200px;
    width: 1050px;
    height: 600px;
    box-shadow: 0 6px 18px rgba(0,0,0,0.18);
  }
  .business-card svg { display: block; }
  .card-text { font-family: "Exo 2", sans-serif; }
  .company-name { fill: var(--white); font-weight: 500; font-size: 21px; }
  .person-name { fill: var(--ink-navy); font-weight: 700; font-size: 38px; }
  .phone-line { fill: var(--ink-navy); font-weight: 400; font-size: 27px; }
  .address-line { fill: var(--ink-navy); font-weight: 400; font-size: 31px; }
  .partner-name { fill: var(--partner-blue); font-weight: 700; font-size: 24px; }
  .partner-line { fill: var(--white); font-weight: 400; font-size: 18px; }
</style>
</head>
<body>
  <div class="business-card">
    <svg width="1050" height="600" viewBox="0 0 1050 600" class="card-text">
      <rect class="card-base" width="1050" height="600" fill="var(--slate)"/>
      <polygon class="partner-field" points="640,0 1050,0 1050,420 706.5,420" fill="var(--panel-grey)"/>
      <polygon class="name-band" points="0,150 663.8,150 675.6,225 0,225" fill="var(--band-light)"/>
      <rect class="phone-tab" x="400" y="252" width="262" height="44" fill="var(--band-light)"/>
      <rect class="phone-tab" x="400" y="312" width="262" height="44" fill="var(--band-light)"/>
      <rect class="phone-tab" x="400" y="372" width="262" height="44" fill="var(--band-light)"/>
      <polygon class="address-band" points="0,520 722.3,520 735,600 0,600" fill="var(--band-light)"/>

      <text class="company-name" x="610" y="70" text-anchor="end">RTV Harbor Management</text>
      <text class="company-name" x="610" y="98" text-anchor="end">Group, LP.</text>

      <text class="person-name" x="590" y="202" text-anchor="end">Darnell Quibey</text>

      <text class="phone-line" x="418" y="283">C : 615-302-4418</text>
      <text class="phone-line" x="418" y="343">D : 615-719-2083</text>
      <text class="phone-line" x="418" y="403">F : 615-864-3371</text>

      <text class="address-line" x="30" y="571">287 Wexford Avenue Lebanon, TN 37185</text>

      <circle class="partner-dot" cx="780" cy="360" r="17" fill="var(--ink-navy)"/>
      <text class="partner-name" x="806" y="369">Velor Hotel Group</text>

      <text class="partner-line" x="878" y="476" text-anchor="middle">“Strategic Partner of Velor Hotel Group”</text>
      <text class="partner-line" x="878" y="508" text-anchor="middle">www.velorhotelgroup-example.com</text>
    </svg>
  </div>
</body>
</html>
```